Brightmend Outdoor Signage

We need an outdoor signage design for my company with new logo designed from artflockhub. We do electrical, Air conditioning & Plumbing, installation, service, repairs and maintenance. The design shall be an eye catching that cannot miss ready it.

Industry/Entity Type

Electrical, Air conditioning, Plumbing

```html
<!DOCTYPE html>
<html lang="en">
<head>
<meta charset="utf-8">
<title>Brightmend Outdoor Signage</title>
<link rel="stylesheet" href="https://fonts.googleapis.com/css2?family=Montserrat:wght@500;600;700;800&display=swap">
<style>
  :root {
    --blue: #2561a8;
    --blue-deep: #1f4f92;
    --red: #e3222b;
    --orange: #ec8a3a;
    --orange-deep: #e8552e;
    --white: #ffffff;
    --stage: #dcdcdc;
  }
  * { margin: 0; padding: 0; box-sizing: border-box; }
  html, body { width: 1200px; height: 925px; overflow: hidden; }
  body { background: var(--stage); font-family: "Montserrat", sans-serif; position: relative; }
  .sign { position: absolute; left: 0; top: 162px; width: 1200px; height: 600px; overflow: hidden; }
  .sign-art { position: absolute; inset: 0; }
  .website { position: absolute; right: 55px; top: 62px; color: var(--white); font-size: 34px; font-weight: 500; display: flex; align-items: center; gap: 10px; white-space: nowrap; }
  .website b { font-weight: 800; }
  .brand { position: absolute; left: 120px; top: 200px; width: 370px; text-align: center; }
  .brand-row { display: flex; align-items: center; justify-content: center; gap: 10px; }
  .brand-dot { width: 22px; height: 22px; border-radius: 50%; background: var(--red); flex: none; }
  .brand-name { color: var(--orange); font-size: 54px; font-weight: 700; letter-spacing: -1px; line-height: 1.1; }
  .brand-tagline { color: var(--blue); font-size: 14px; font-weight: 700; margin-top: 6px; word-spacing: 4px; white-space: nowrap; }
  .mascot { position: absolute; left: 478px; top: 236px; width: 136px; height: 356px; border-radius: 60px 60px 20px 20px; background: linear-gradient(180deg, #f0d9c4 0%, #3e74c0 35%, #2a5ea6 100%); }
  .pill { position: absolute; left: 799px; top: 310px; width: 192px; height: 46px; border-radius: 23px; background: var(--white); color: var(--red); font-size: 21px; font-weight: 800; display: flex; align-items: center; justify-content: center; }
  .services { position: absolute; list-style: none; }
  .services li { display: flex; align-items: center; gap: 14px; color: var(--white); font-size: 26px; font-weight: 600; height: 40px; white-space: nowrap; }
  .services-main { left: 624px; top: 377px; }
  .services-main li + li { margin-top: 14px; }
  .services-extra { left: 946px; top: 385px; }
  .services-extra li + li { margin-top: 15px; }
  .icon { width: 40px; height: 40px; flex: none; }
  .phone { position: absolute; left: 36px; top: 516px; color: var(--white); font-size: 48px; font-weight: 800; display: flex; align-items: center; gap: 8px; letter-spacing: -0.5px; white-space: nowrap; }
</style>
</head>
<body>
<section class="sign">
  <svg class="sign-art" viewBox="0 0 1200 600" width="1200" height="600">
    <defs>
      <linearGradient id="orangeSky" x1="0" y1="1" x2="1" y2="0">
        <stop offset="0" stop-color="#e8432c"/>
        <stop offset="1" stop-color="#ed8a3b"/>
      </linearGradient>
      <linearGradient id="whiteSweep" x1="0" y1="0" x2="1" y2="0">
        <stop offset="0" stop-color="#ffffff" stop-opacity="0.2"/>
        <stop offset="1" stop-color="#ffffff"/>
      </linearGradient>
      <radialGradient id="iconFill" cx="0.4" cy="0.35" r="0.7">
        <stop offset="0" stop-color="#f39a3a"/>
        <stop offset="1" stop-color="#e3322b"/>
      </radialGradient>
    </defs>
    <rect class="backdrop" width="1200" height="600" fill="url(#orangeSky)"/>
    <path class="top-blue-line" d="M560 440 C760 300 900 170 1200 130 V180 C980 180 820 290 600 440 Z" fill="var(--blue)"/>
    <path class="white-sweep" d="M560 450 C760 320 920 190 1200 165 V252 C1000 200 840 300 600 460 Z" fill="url(#whiteSweep)"/>
    <circle class="badge-ring" cx="324" cy="118" r="322" fill="var(--red)"/>
    <circle class="badge-face" cx="324" cy="118" r="306" fill="var(--white)"/>
    <path class="blue-ground" d="M0 290 C120 400 280 470 470 470 C640 460 760 390 880 320 C1000 260 1100 230 1200 252 V600 H0 Z" fill="var(--blue)"/>
    <path class="ground-shine" d="M10 320 C140 430 300 470 470 475" fill="none" stroke="#ffffff" stroke-opacity="0.35" stroke-width="5"/>
  </svg>

  <div class="website">
    <svg width="32" height="32" viewBox="0 0 34 34" aria-hidden="true"><g fill="none" stroke="#fff" stroke-width="2"><circle cx="17" cy="17" r="15"/><circle cx="17" cy="17" r="10"/><ellipse cx="17" cy="17" rx="4.5" ry="10"/><line x1="7" y1="17" x2="27" y2="17"/></g></svg>
    <span>www.<b>brightmend</b>.com</span>
  </div>

  <div class="brand">
    <div class="brand-row"><span class="brand-dot"></span><span class="brand-name">Brightmend</span></div>
    <p class="brand-tagline">Electrical Air Conditioning Plumbing</p>
  </div>

  <div class="mascot" role="img" aria-label="Cartoon handyman in blue overalls and cap holding a pipe wrench over his shoulder"></div>

  <div class="pill">What We Do</div>

  <ul class="services services-main">
    <li><svg class="icon" viewBox="0 0 40 40"><circle cx="20" cy="20" r="19" fill="url(#iconFill)" stroke="#fff" stroke-width="2"/><path d="M22 9 L13 22 H19 L17 31 L27 17 H21 Z" fill="#fff"/></svg>Electrical</li>
    <li><svg class="icon" viewBox="0 0 40 40"><circle cx="20" cy="20" r="19" fill="url(#iconFill)" stroke="#fff" stroke-width="2"/><g stroke="#fff" stroke-width="2"><line x1="20" y1="10" x2="20" y2="30"/><line x1="11" y1="15" x2="29" y2="25"/><line x1="11" y1="25" x2="29" y2="15"/></g></svg>Air Conditioning</li>
    <li><svg class="icon" viewBox="0 0 40 40"><circle cx="20" cy="20" r="19" fill="url(#iconFill)" stroke="#fff" stroke-width="2"/><path d="M12 16 H24 V22 H20 V18 H12 Z M17 12 H21 V16 H17 Z" fill="#fff"/><circle cx="22" cy="28" r="2.5" fill="#fff"/></svg>Plumbing</li>
    <li><svg class="icon" viewBox="0 0 40 40"><circle cx="20" cy="20" r="19" fill="url(#iconFill)" stroke="#fff" stroke-width="2"/><circle cx="20" cy="20" r="8" fill="none" stroke="#fff" stroke-width="3" stroke-dasharray="4 2"/><path d="M16 20 L19 23 L24 17" fill="none" stroke="#fff" stroke-width="2"/></svg>Installation</li>
  </ul>

  <ul class="services services-extra">
    <li><svg class="icon" viewBox="0 0 40 40"><circle cx="20" cy="20" r="19" fill="url(#iconFill)" stroke="#fff" stroke-width="2"/><circle cx="17" cy="20" r="7" fill="none" stroke="#fff" stroke-width="3" stroke-dasharray="3 2"/><rect x="24" y="12" width="4" height="16" rx="2" fill="#fff"/></svg>Service</li>
    <li><svg class="icon" viewBox="0 0 40 40"><circle cx="20" cy="20" r="19" fill="url(#iconFill)" stroke="#fff" stroke-width="2"/><g stroke="#fff" stroke-width="3" stroke-linecap="round"><line x1="12" y1="12" x2="28" y2="28"/><line x1="28" y1="12" x2="12" y2="28"/></g></svg>Repairs</li>
    <li><svg class="icon" viewBox="0 0 40 40"><circle cx="20" cy="20" r="19" fill="url(#iconFill)" stroke="#fff" stroke-width="2"/><g stroke="#fff" stroke-width="3" stroke-linecap="round"><line x1="12" y1="28" x2="26" y2="14"/><circle cx="27" cy="13" r="3" fill="none"/></g></svg>Maintenance</li>
  </ul>

  <div class="phone">
    <svg width="36" height="36" viewBox="0 0 36 36" aria-hidden="true"><circle cx="18" cy="18" r="16" fill="none" stroke="#fff" stroke-width="2"/><path d="M12 10 L15 10 L16 14 L14 16 C15 19 17 21 20 22 L22 20 L26 21 L26 24 C26 25 25 26 24 26 C17 26 10 19 10 12 C10 11 11 10 12 10 Z" fill="#fff"/></svg>
    <span>4512 555 019</span>
  </div>
</section>
</body>
</html>
```